Create for us a Shop-Stopper Business Card

We need a standout, first class business card to go along with our new brand strategy. Sleek, Contemporary and fresh.

Colors and theme must sync with our websitewww.pelvorpower.co.uk

We want a business card that has a global brand appeal. TKR Energy is a small UK renewable company that specialises in energy projects in Africa. We want a business card that has the following characteristics: Very short, precise, global, stand out, NOT TOO LOUD but contemporary. The company's colour themes are White, Grey with a hint of green.

Target Market(s)

Business exec, high net worth individuals, investors, commercial leaders, suppliers, government officials

Industry/Entity Type

Solar Energy

Contact Information for Business Card

Logo, Name, Title, Address, web address, email,

Requirements
Must have
• Logo must be sharp
Nice to have
• Adapt fonts from the logo. The large circular side of the logo at the back in a very refreshing way
Should not have
• No solar panel shapes or image.Very little black. If possible avoid black. Its not coming out nice. I think !!!

```html
<!DOCTYPE html>
<html lang="en">
<head>
<meta charset="utf-8">
<title>TKR Energy Business Card</title>
<link href="https://fonts.googleapis.com/css2?family=Questrial&family=Arimo:wght@400;700&display=swap" rel="stylesheet">
<style>
  :root {
    --backdrop: #2e2f31;
    --card-dark: #2a2b2d;
    --card-light: #ffffff;
    --green-deep: #0b6a2c;
    --green-mid: #1e8a3a;
    --rule-red: #c8343a;
    --ink-grey: #4a4a4c;
    --soft-grey: #6b6b6e;
    --white: #ffffff;
  }
  html, body {
    margin: 0;
    padding: 0;
    width: 1200px;
    height: 843px;
    overflow: hidden;
    background: var(--backdrop);
  }
  .canvas {
    width: 1200px;
    height: 843px;
    display: flex;
    align-items: center;
    justify-content: center;
    gap: 40px;
  }
  .card {
    width: 560px;
    height: 320px;
    display: block;
    border-radius: 4px;
    box-shadow: 0 10px 30px rgba(0,0,0,0.35);
  }
  .brand-name { font-family: "Questrial", sans-serif; letter-spacing: 1px; }
  .person-name { font-family: "Arimo", sans-serif; font-weight: 700; }
  .person-title { font-family: "Arimo", sans-serif; }
  .contact { font-family: "Arimo", sans-serif; font-size: 13px; fill: var(--white); }
</style>
</head>
<body>
<main class="canvas">

  <!-- Back of card -->
  <svg class="card card-back" viewBox="0 0 560 320" xmlns="http://www.w3.org/2000/svg">
    <rect width="560" height="320" rx="4" fill="var(--card-dark)"/>
    <circle class="brand-dot" cx="128" cy="150" r="24" fill="none" stroke="var(--white)" stroke-width="6"/>
    <text class="brand-name" x="168" y="164" font-size="40" fill="var(--white)">TKR ENERGY</text>
    <line class="brand-rule" x1="168" y1="180" x2="452" y2="180" stroke="var(--white)" stroke-width="1.5"/>
    <text class="contact back-web" x="280" y="238" text-anchor="middle" letter-spacing="4">www.pelvorpower.co.uk</text>
  </svg>

  <!-- Front of card -->
  <svg class="card card-front" viewBox="0 0 560 320" xmlns="http://www.w3.org/2000/svg">
    <defs>
      <linearGradient id="band-green" x1="0" y1="0" x2="1" y2="1">
        <stop offset="0" stop-color="var(--green-mid)"/>
        <stop offset="1" stop-color="var(--green-deep)"/>
      </linearGradient>
    </defs>
    <rect width="560" height="320" rx="4" fill="var(--card-light)"/>

    <!-- Plain footer band -->
    <rect class="footer-band" x="0" y="196" width="560" height="124" fill="url(#band-green)"/>

    <!-- Brand -->
    <circle class="brand-dot" cx="48" cy="60" r="20" fill="none" stroke="var(--green-mid)" stroke-width="6"/>
    <text class="brand-name" x="80" y="73" font-size="36" fill="var(--ink-grey)">TKR ENERGY</text>
    <line class="brand-rule" x1="80" y1="84" x2="306" y2="84" stroke="var(--rule-red)" stroke-width="1.2"/>

    <!-- Person -->
    <text class="person-name" x="42" y="128" font-size="17" fill="var(--green-mid)">ALAN MERROW</text>
    <text class="person-title" x="42" y="147" font-size="13" fill="var(--soft-grey)">PRESIDENT</text>

    <!-- Contact -->
    <text class="contact" x="530" y="222" text-anchor="end">4127 Harlow Crescent</text>
    <text class="contact" x="530" y="239" text-anchor="end">Glen Ridge, NY 11020</text>
    <text class="contact" x="520" y="264" text-anchor="end">555 0142 7788</text>
    <text class="contact" x="520" y="283" text-anchor="end">alan@pelvorpower.co.uk</text>
    <text class="contact" x="520" y="302" text-anchor="end">www.pelvorpower.co.uk</text>

    <!-- Icons -->
    <g class="icon icon-phone" fill="var(--white)">
      <path d="M527,254 h14 a2,2 0 0 1 2,2 v2 h-4 v-2 h-10 v2 h-4 v-2 a2,2 0 0 1 2,-2 Z"/>
      <rect x="529" y="259" width="12" height="6" rx="1"/>
    </g>
    <g class="icon icon-mail">
      <rect x="527" y="274" width="16" height="11" rx="1" fill="var(--white)"/>
      <path d="M527,275 L535,281 L543,275" fill="none" stroke="var(--green-deep)" stroke-width="1.2"/>
    </g>
    <g class="icon icon-web">
      <circle cx="535" cy="298" r="7" fill="var(--white)"/>
      <ellipse cx="535" cy="298" rx="3" ry="7" fill="none" stroke="var(--green-deep)" stroke-width="1"/>
      <line x1="528" y1="298" x2="542" y2="298" stroke="var(--green-deep)" stroke-width="1"/>
    </g>
  </svg>

</main>
</body>
</html>
```